Plumvale CEO needs a Crowdsourced Graphic for a Wirelark Article

I need a simple graphic / banner for a blog post that's going to be posted on Wirelark (www.wirelark.com) - the biggest tech blog in the world.

The article will be written by Tobin Marsh (Plumvale's CEO) and the title will be "Asia's Secret Crowdsourcing Boom". The article is about the tens of thousands of people using crowdsourcing websites (like Plumvale.com, Qorvel.com and Vantrio.com) in China, India, the Philippines, Australia and other countries in the Asia Pacific region.

We'd really like to get this ASAP - so early submissions encouraged. We will try and get the winning designer linked to from the article.

Thanks to everyone that submitted!  Some great designs and hard to choose! :)

Target Market(s)

Tech saavy readers, English speakers

Industry/Entity Type

Tech

Requirements
Must have
• The graphic SHOULD:
1) Have the text "Asia's secret crowdsourcing boom" with some nice design and fonts (consider grey subtle pattern background and white drop shadow on fonts) - see attached examples
2) Have an Asian theme
3) Have the dimensions 640px wide by 240px wide
Nice to have
• The graphic COULD:
1) Have references to some or all of the countries mentioned above or use Asian characters as part of the background / motif (maybe the word "crowd" or "crowd sourcing" in different languages). In Chinese, the word for crowdsourcing is "witkey" (and there are corresponding Chinese characters: ??)
2) Emphasize the word "Asia" (using color and larger/different font)
3) Use a chart showing exponential (i.e. fast) growth - like the attached
4) Have a second line of text "5 Things You Didn't Know About Crowdsourcing in Asia"

```html
<!DOCTYPE html>
<html lang="en">
<head>
<meta charset="utf-8">
<title>Asia's Secret Crowdsourcing Boom</title>
<link rel="stylesheet" href="https://fonts.googleapis.com/css2?family=Cinzel+Decorative:wght@700&family=Roboto:wght@400;500&display=swap">
<style>
  :root {
    --paper: #e3e3e1;
    --paper-dark: #d2d2d0;
    --asia-teal: #3cbfd3;
    --asia-edge: #1f8ea3;
    --navy: #1c2747;
    --ink: #111111;
    --line-teal: #2b9db4;
    --bar-purple: #a65aa8;
    --band-teal: #24a9c2;
    --band-foot: #cfcfcd;
    --plate-blue: #2c3f86;
    --plate-light: #e8ecf4;
    --white: #ffffff;
  }
  html, body {
    margin: 0;
    padding: 0;
    width: 1200px;
    height: 450px;
    overflow: hidden;
    background: var(--paper);
  }
  .banner {
    position: relative;
    width: 1200px;
    height: 450px;
    overflow: hidden;
    background:
      radial-gradient(circle at 1px 1px, rgba(0,0,0,0.05) 1px, transparent 1.5px) 0 0 / 4px 4px,
      linear-gradient(180deg, var(--paper) 0%, var(--paper-dark) 100%);
  }
  .plate-ornament {
    position: absolute;
    left: 815px;
    top: -235px;
    width: 620px;
    height: 620px;
    border-radius: 50%;
    background: radial-gradient(circle, var(--plate-light) 0%, #b9c3dc 45%, var(--plate-blue) 100%);
  }
  .growth-chart {
    position: absolute;
    left: 0;
    top: 0;
  }
  .title-asia {
    position: absolute;
    left: 26px;
    top: 2px;
    margin: 0;
    font-family: "Cinzel Decorative", serif;
    font-weight: 700;
    font-size: 92px;
    line-height: 1;
    color: var(--asia-teal);
    -webkit-text-stroke: 1.5px var(--asia-edge);
    text-shadow: 2px 2px 0 var(--white);
  }
  .title-secret {
    position: absolute;
    left: 372px;
    top: 4px;
    margin: 0;
    font-family: "Roboto", sans-serif;
    font-weight: 400;
    font-size: 104px;
    line-height: 1;
    color: var(--navy);
    text-shadow: 2px 2px 0 var(--white);
  }
  .title-sub {
    position: absolute;
    left: 28px;
    top: 116px;
    margin: 0;
    font-family: "Roboto", sans-serif;
    font-weight: 500;
    font-size: 54px;
    line-height: 1;
    color: var(--ink);
    text-shadow: 2px 2px 0 var(--white);
  }
  .tagline-band {
    position: absolute;
    left: 0;
    top: 383px;
    width: 1200px;
    height: 52px;
    background: var(--band-teal);
    display: flex;
    align-items: center;
  }
  .tagline {
    margin: 0 0 0 28px;
    font-family: "Roboto", sans-serif;
    font-weight: 400;
    font-size: 37px;
    color: var(--white);
    white-space: nowrap;
  }
  .band-foot {
    position: absolute;
    left: 0;
    top: 435px;
    width: 1200px;
    height: 15px;
    background: var(--band-foot);
  }
</style>
</head>
<body>
  <div class="banner">
    <div class="plate-ornament" role="img" aria-label="Blue and white Asian porcelain plate with floral pattern"></div>

    <svg class="growth-chart" width="1200" height="450" viewBox="0 0 1200 450" aria-hidden="true">
      <g stroke="var(--bar-purple)" stroke-width="1.6">
        <path d="M38 367.8V383M57 364.2V383M76 360.6V383M95 357V383M114 353.4V383M133 349.8V383M152 346.2V383
                 M171 342.7V383M190 339.6V383M209 336.4V383M228 333.3V383M247 330.2V383M266 327.1V383M285 324V383
                 M304 315.9V383M323 305.5V383M342 295V383M361 284.6V383M380 274.2V383
                 M399 268.9V383M418 265.1V383M437 261.2V383M456 257.3V383M475 253.4V383M494 249.5V383M513 245.6V383
                 M532 240.9V383M551 235.6V383M570 230.3V383M589 224.9V383M608 219.6V383M627 214.3V383M646 209V383M665 203.6V383M684 198.3V383
                 M722 185.1V383M741 177.1V383M760 169.2V383M779 161.3V383M798 153.3V383"/>
      </g>
      <polyline points="0,375 169,343 291,323 384,272 521,244 703,193 806,150"
                fill="none" stroke="var(--line-teal)" stroke-width="5" stroke-linejoin="round"/>
      <g fill="var(--line-teal)">
        <circle cx="169" cy="343" r="8"/>
        <circle cx="291" cy="323" r="8"/>
        <circle cx="384" cy="272" r="8"/>
        <circle cx="521" cy="244" r="8"/>
        <circle cx="703" cy="193" r="8"/>
      </g>
    </svg>

    <h1 class="title-asia">ASIA'S</h1>
    <p class="title-secret">Secret</p>
    <p class="title-sub">crowdsourcing boom</p>

    <div class="tagline-band">
      <p class="tagline">5 Things You Didn’t Know About Crowdsourcing in Asia</p>
    </div>
    <div class="band-foot"></div>
  </div>
</body>
</html>
```